eCommerce Landing Page Design for Wine Accessories using PageFly

Need to develop a landing page template that can be used for ecommerce products. This template needs to be built in PageFly (shopify App) if not in Pagefly, need an integrated app with shopify to maintain the correct url. The website is www.bluemarrowden.com. The template will be built using one product as an example. Copy and product images will be provided. the Landing page also must have "15% Off" and "free shipping" somewhere on the page

Although part of a website, I am open to different options on design

Target Market(s)

Wine drinkers

Requirements
Must have
• Built in PageFly (shopify App)
• Featured Product
• 15% Off
• Free Shipping
• High Converting with add to cart actions directly on the page

```html
<!DOCTYPE html>
<html lang="en">
<head>
<meta charset="utf-8">
<title>Cork Hour Club — Wine Accessories</title>
<link href="https://fonts.googleapis.com/css2?family=Playfair+Display:wght@400;700&family=Open+Sans:wght@400;600;700&display=swap" rel="stylesheet">
<style>
  :root{
    --wine:#a3061d;
    --wine-1:#c8102e;
    --wine-2:#b30c27;
    --wine-3:#9a0a21;
    --wine-4:#7c0616;
    --ink:#333333;
    --muted:#555555;
    --paper:#ffffff;
    --line:#d9d9d9;
  }
  *{box-sizing:border-box;margin:0;padding:0}
  html,body{width:1200px;height:3203px;overflow:hidden;background:var(--paper)}
  body{position:relative;font-family:"Open Sans",Arial,sans-serif;color:var(--ink)}
  .abs{position:absolute}
  .serif{font-family:"Playfair Display",Georgia,serif}

  /* hero */
  .hero{left:0;top:0;width:1200px;height:615px;background:linear-gradient(100deg,#5a3a2c 0%,#8a6a58 30%,#b7a9a0 55%,#6d4b5e 75%,#cfc3b8 100%)}
  .topbar{left:0;top:0;width:1200px;height:90px;color:#fff;font-weight:700;font-size:16px;letter-spacing:.5px}
  .menu{left:24px;top:34px;display:flex;align-items:center;gap:10px}
  .topbar-name{left:0;width:1200px;top:30px;text-align:center;font-family:"Playfair Display",Georgia,serif;font-size:26px;font-weight:400;color:#fff}
  .shop{right:36px;top:34px;display:flex;align-items:center;gap:26px}
  .brand-disc{left:412px;top:122px;width:376px;height:376px;border-radius:50%;background:rgba(30,30,30,.72)}
  .brand-name{left:412px;top:268px;width:376px;text-align:center;color:#fff;font-family:"Playfair Display",Georgia,serif;font-size:54px;font-weight:400;line-height:1.1}
  .arrow{top:290px}

  /* welcome */
  .welcome{left:132px;top:534px;width:936px;padding-top:44px;text-align:center;background:var(--paper)}
  .welcome h1{font-family:"Playfair Display",Georgia,serif;font-weight:400;color:var(--wine);font-size:34px}
  .welcome p{font-size:15px;color:var(--muted);line-height:24px;margin-top:14px;padding:0 40px}
  .welcome p + p{margin-top:24px}

  .section-title{left:0;width:1200px;text-align:center;font-family:"Playfair Display",Georgia,serif;color:var(--wine);font-size:34px;font-weight:400}

  /* products */
  .products{left:132px;top:856px;width:936px;height:369px;display:flex}
  .product{width:234px;height:369px;position:relative}
  .product-photo{height:273px}
  .product-info{height:96px;color:#fff;text-align:center;padding:20px 10px 0;font-family:"Playfair Display",Georgia,serif}
  .product-info h3{font-size:11px;font-weight:400;text-transform:uppercase;line-height:16px}
  .product-info .price{font-size:14px;margin-top:8px}
  .price s{opacity:.75;margin-right:6px}
  .p1 .product-info{background:var(--wine-1)}
  .p2 .product-info{background:var(--wine-2)}
  .p3 .product-info{background:var(--wine-3)}
  .p4 .product-info{background:var(--wine-4)}
  .add-cart{position:absolute;left:58px;top:117px;width:120px;height:40px;background:#222;color:#fff;font-size:13px;display:flex;align-items:center;justify-content:center;gap:8px;border-radius:2px}

  /* gallery */
  .tile{position:absolute}
  .thumbs{left:132px;top:2169px;width:936px;height:160px;display:flex}
  .thumbs div{flex:1}

  /* promos */
  .promo{top:2378px;width:468px;height:479px}
  .promo-photo{height:239px}
  .promo-body{height:240px;background:var(--wine);color:#fff;text-align:center;padding:38px 22px 0}
  .promo-body h2{font-family:"Playfair Display",Georgia,serif;font-weight:400;font-size:24px}
  .promo-body p{font-size:11.5px;line-height:21px;text-align:left;margin-top:18px;opacity:.9}
  .promo-body .more{font-size:12px;font-weight:700;margin-top:20px;display:inline-flex;align-items:center;gap:6px}

  /* newsletter + footer */
  .signup{left:420px;top:2965px;width:359px;height:43px;display:flex}
  .signup .field{width:248px;border:1px solid var(--line);font-size:11px;color:#777;padding:14px 16px}
  .signup .go{flex:1;background:var(--wine);display:flex;align-items:center;justify-content:center}
  .foot-links{left:0;width:1200px;top:3040px;text-align:center;font-size:12px;color:#666;letter-spacing:.5px;word-spacing:20px}
  .social{left:529px;top:3072px;display:flex;gap:20px}
  .social span{width:14px;height:14px;border-radius:50%;background:#666}
  .copy{left:0;width:1200px;top:3120px;text-align:center;font-size:12px;color:#666}
  .cards{left:530px;top:3152px;display:flex;gap:6px}
  .cards span{width:24px;height:15px;border-radius:2px;background:#b9c3d2}
  .ver{right:12px;top:3180px;font-size:10px;color:#888}
</style>
</head>
<body>

<!-- Hero -->
<div class="abs hero" role="img" aria-label="Row of coloured stemmed stainless wine tumblers on a table with flowers"></div>
<div class="abs topbar">
  <div class="abs menu">
    <svg width="16" height="14" viewBox="0 0 16 14"><rect y="0" width="16" height="2.4" fill="#fff"/><rect y="5.8" width="16" height="2.4" fill="#fff"/><rect y="11.6" width="16" height="2.4" fill="#fff"/></svg>
    MENU
  </div>
  <div class="abs topbar-name">Cork Hour</div>
  <div class="abs shop">
    SHOP
    <svg width="18" height="18" viewBox="0 0 18 18"><circle cx="7.5" cy="7.5" r="5.5" fill="none" stroke="#fff" stroke-width="2.4"/><line x1="11.5" y1="11.5" x2="17" y2="17" stroke="#fff" stroke-width="2.6"/></svg>
    <svg width="20" height="17" viewBox="0 0 20 17"><path d="M1 6h18l-2.5 10h-13z" fill="#fff"/><path d="M5 6l4-5M15 6l-4-5" stroke="#fff" stroke-width="1.8" fill="none"/></svg>
  </div>
</div>
<div class="abs brand-disc"></div>
<div class="abs brand-name">Cork Hour Club</div>
<svg class="abs arrow" style="left:38px" width="16" height="28" viewBox="0 0 16 28"><path d="M14 2L3 14l11 12" fill="none" stroke="#fff" stroke-width="3"/></svg>
<svg class="abs arrow" style="right:38px" width="16" height="28" viewBox="0 0 16 28"><path d="M2 2l11 12L2 26" fill="none" stroke="#fff" stroke-width="3"/></svg>

<!-- Welcome -->
<section class="abs welcome">
  <h1>Welcome To Cork Hour Club</h1>
  <p>Aliquam erat volutpat. Etiam quis aliquet risus. Duis ornare erat eget magna dapibus.</p>
  <p>Nam tempus, quam in bibendum vulputate, sapien dolor viverra nisl, vitae euismod elit turpis et nulla. Aliquam erat volutpat. Pellentesque blandit lacus eget nunc faucibus, et tincidunt eros viverra. Phasellus consequat sagittis nisi.</p>
</section>

<!-- Featured products -->
<h2 class="abs section-title" style="top:790px">Featured Products</h2>
<div class="abs products">
  <article class="product p1">
    <div class="product-photo" role="img" aria-label="Silver stemmed insulated wine glass" style="background:linear-gradient(160deg,#eef0f2,#b9bcc0 60%,#e9e6df)"></div>
    <div class="add-cart">
      <svg width="13" height="12" viewBox="0 0 13 12"><path d="M0 1h2.5l2 7h7l1.5-5H4" fill="none" stroke="#fff" stroke-width="1.6"/><circle cx="5" cy="10.5" r="1.2" fill="#fff"/><circle cx="10.5" cy="10.5" r="1.2" fill="#fff"/></svg>
      Add to cart
    </div>
    <div class="product-info"><h3>New 10oz Stainless Double Wall<br>Insulated Wine Glass</h3><div class="price"><s>$34.95</s>$24.95</div></div>
  </article>
  <article class="product p2">
    <div class="product-photo" role="img" aria-label="Red stemmed stainless wine cup" style="background:linear-gradient(160deg,#f3e4c8,#d8202a 55%,#e9dcc2)"></div>
    <div class="product-info"><h3>Stainless Steel 9 oz. Wine Cup w/<br>Lid No Sweat Stays Cold</h3><div class="price">$17.95</div></div>
  </article>
  <article class="product p3">
    <div class="product-photo" role="img" aria-label="Purple stemmed wine cup" style="background:linear-gradient(160deg,#f3e4c8,#7c2a9a 55%,#e9dcc2)"></div>
    <div class="product-info"><h3>High Quality Silicone Elegant<br>Design Wine Aerator Pour Spout</h3><div class="price">$3.95</div></div>
  </article>
  <article class="product p4">
    <div class="product-photo" role="img" aria-label="Mint green stemmed wine cup" style="background:linear-gradient(160deg,#f3e4c8,#5fd1a9 55%,#e9dcc2)"></div>
    <div class="product-info"><h3>2018 Ceative Funny Wine Glass<br>Crystal Wine Stopper Glass</h3><div class="price">$19.95</div></div>
  </article>
</div>

<!-- Gallery -->
<div class="tile" style="left:132px;top:1275px;width:468px;height:318px;background:linear-gradient(135deg,#7a5030,#b49ae0 45%,#3b4fc4 75%,#6b4428)" role="img" aria-label="Lilac and blue insulated wine tumblers on a wooden table"></div>
<div class="tile" style="left:600px;top:1275px;width:468px;height:318px;background:linear-gradient(135deg,#c9a27a,#f2f2f2 45%,#a5182a 65%,#8b6a4b)" role="img" aria-label="Phone case printed with a glass of red wine and a drink slogan"></div>
<div class="tile" style="left:132px;top:1593px;width:936px;height:529px;background:radial-gradient(ellipse at 50% 55%,#6a3a1e 0%,#3a1e10 40%,#c7c7c7 70%)" role="img" aria-label="Four panel canvas print of a wine barrel, bottle and glass of red wine"></div>

<div class="abs thumbs">
  <div role="img" aria-label="Stainless steel beer mugs" style="background:linear-gradient(#f2f2f2,#b8bcc0)"></div>
  <div role="img" aria-label="Double wall glass with amber drink" style="background:linear-gradient(#efe6d8,#c38a42)"></div>
  <div role="img" aria-label="Wine bottle and cork holder" style="background:linear-gradient(#e8ddd0,#5a3a28)"></div>
  <div role="img" aria-label="Wall mounted wine bottle rack" style="background:linear-gradient(#f4f4f4,#7d8f5a)"></div>
  <div role="img" aria-label="Tabletop wine rack with bottles" style="background:linear-gradient(#f0f0f0,#5a2a2a)"></div>
</div>

<!-- Promotions -->
<div class="abs promo" style="left:132px">
  <div class="promo-photo" role="img" aria-label="Dotted coloured wine glasses on a dark background" style="background:linear-gradient(90deg,#1c1c22,#3a8fc9 35%,#c01b2a 65%,#2a2fb8 90%,#1c1c22)"></div>
  <div class="promo-body">
    <h2>15% Off</h2>
    <p>Fusce eget neque elit. Sed augue orci, elementum in magna congue, tincidunt vulputate erat. Aliquam consectetur orci molestie dictum molestie. Proin eget congue nulla, vel tempor diam. Ut non ante est.</p>
    <div class="more">Read More <svg width="10" height="10" viewBox="0 0 10 10"><path d="M0 5h7M4 1.5L8 5 4 8.5" fill="none" stroke="#fff" stroke-width="2"/></svg></div>
  </div>
</div>
<div class="abs promo" style="left:600px">
  <div class="promo-photo" role="img" aria-label="Glass of red wine with a red rose on a dark table" style="background:radial-gradient(ellipse at 55% 60%,#6a0d18 0%,#262626 45%,#1a1a1a 100%)"></div>
  <div class="promo-body">
    <h2>Free Shipping</h2>
    <p>Fusce eget neque elit. Sed augue orci, elementum in magna congue, tincidunt vulputate erat. Aliquam consectetur orci molestie dictum molestie. Proin eget congue nulla, vel tempor diam. Ut non ante est.</p>
    <div class="more">Read More <svg width="10" height="10" viewBox="0 0 10 10"><path d="M0 5h7M4 1.5L8 5 4 8.5" fill="none" stroke="#fff" stroke-width="2"/></svg></div>
  </div>
</div>

<!-- Newsletter -->
<h2 class="abs section-title" style="top:2922px;font-size:26px">Signup to our newsletter</h2>
<form class="abs signup">
  <div class="field">Email Address</div>
  <div class="go"><svg width="14" height="14" viewBox="0 0 14 14"><path d="M1 7h10M7 2.5L11.5 7 7 11.5" fill="none" stroke="#fff" stroke-width="2.4"/></svg></div>
</form>

<!-- Footer -->
<nav class="abs foot-links">SEARCH CONTACT BLOG</nav>
<div class="abs social"><span></span><span></span><span></span><span></span></div>
<p class="abs copy">Copyright © 2018 Cork Hour Club. All rights reserved</p>
<div class="abs cards"><span></span><span></span><span></span><span></span><span></span></div>
<div class="abs ver">M2</div>

</body>
</html>
```